QVD Postcard design

Would like a postcard designed that can be distributed to places of business. The postcard should have our logo and the following written on the front "How much are you loosing.....?" and on the back the following
....due to poor signals, Mobile Phone/WIFI/Internet?
then below that have 3 points, one covering each of the following:

Mobile signal boosting
We’ve all been there! Dropped calls, black spots in buildings…… we carry out a detailed survey to work out the best location for getting a mobile signal and when we find it we provide a solution to boost it around your building – it’s like magic and ZANTIK compliant!

WIFI
We’ve come to expect WIFI everywhere and get really frustrated when it doesn’t work. The quorvadetta team love a challenge and design and implement solutions even for the most difficult of circumstances.

Radio and Microwave
When wires under the ground just aren’t possible or are going to take too long to get you up and running, We specialise in bespoke solutions, we can always find a way!

Contact us to see how we can help turn this around quickly

Marek Tollis, Director
e: Marek.tollis@quorvadetta.example / info@quorvadetta.example
w: https://www.quorvadetta.example (could you create this as a QR code?)
t: +44 3309 574 206

```html
<!DOCTYPE html>
<html lang="en">
<head>
<meta charset="utf-8">
<title>quorvadetta – Postcard Front</title>
<link rel="stylesheet" href="https://fonts.googleapis.com/css2?family=League+Spartan:wght@600;700&display=swap">
<style>
  :root {
    --sun: #fcc917;
    --sun-deep: #f5b91a;
    --amber: #f2a531;
    --ink: #000000;
    --night: #0d0f12;
    --night-soft: #1a1c20;
    --olive: #8a7430;
    --white: #ffffff;
  }
  * { margin: 0; padding: 0; box-sizing: border-box; }
  html, body { width: 1200px; height: 861px; overflow: hidden; background: var(--night); }
  .postcard {
    position: relative;
    width: 1200px;
    height: 861px;
    overflow: hidden;
    font-family: "League Spartan", "Futura", sans-serif;
  }
  .backdrop { position: absolute; inset: 0; display: block; }
  .headline {
    position: absolute;
    left: 0; right: 0;
    top: 136px;
    text-align: center;
    color: var(--ink);
    font-weight: 700;
    font-size: 121px;
    line-height: 130px;
    letter-spacing: -0.5px;
  }
  .brand {
    position: absolute;
    left: 46px;
    top: 738px;
    color: var(--white);
  }
  .brand-mark {
    display: flex;
    align-items: center;
    gap: 12px;
  }
  .brand-dot {
    width: 20px; height: 20px;
    border-radius: 50%;
    background: var(--sun-deep);
  }
  .brand-name {
    font-weight: 600;
    font-size: 54px;
    line-height: 1;
    letter-spacing: -1px;
  }
  .brand-tagline {
    margin-top: 12px;
    font-weight: 700;
    font-size: 16.5px;
    letter-spacing: 0.1px;
    white-space: nowrap;
  }
</style>
</head>
<body>
<main class="postcard">
  <svg class="backdrop" width="1200" height="861" viewBox="0 0 1200 861">
    <defs>
      <linearGradient id="photoWash" x1="0" y1="0" x2="1" y2="0">
        <stop offset="0" stop-color="#fcc917"/>
        <stop offset="0.55" stop-color="#f6c320"/>
        <stop offset="1" stop-color="#f8c51c"/>
      </linearGradient>
      <linearGradient id="bandGlow" x1="0" y1="0" x2="1" y2="0">
        <stop offset="0" stop-color="#0b0603" stop-opacity="0"/>
        <stop offset="0.35" stop-color="#3a230a" stop-opacity="0.9"/>
        <stop offset="1" stop-color="#8a7430"/>
      </linearGradient>
      <linearGradient id="amberEdge" x1="0" y1="0" x2="1" y2="0">
        <stop offset="0" stop-color="#f2a531"/>
        <stop offset="1" stop-color="#f2a531" stop-opacity="0"/>
      </linearGradient>
      <radialGradient id="meshGlow" cx="0.7" cy="0.75" r="0.6">
        <stop offset="0" stop-color="#3a3c40"/>
        <stop offset="1" stop-color="#0d0f12"/>
      </radialGradient>
    </defs>

    <rect class="sun-field" x="0" y="0" width="1200" height="628" fill="var(--sun)"/>
    <rect class="photo-wash" x="0" y="0" width="1200" height="560" fill="url(#photoWash)" opacity="0.9"
          role="img" aria-label="Faint yellow-toned photo of two colleagues looking at a tablet in an office"/>

    <polygon points="0,448 280,490 0,480" fill="url(#amberEdge)"/>

    <polygon class="dark-wedge" points="0,478 1200,560 1200,628 0,628" fill="#0b0603"/>
    <polygon class="wedge-glow" points="560,520 1200,560 1200,628 560,628" fill="url(#bandGlow)"/>
    <rect class="wedge-floor" x="0" y="574" width="1200" height="54" fill="var(--night)" opacity="0.85"/>
    <polygon points="620,574 1200,574 1200,628 620,628" fill="url(#bandGlow)" opacity="0.8"/>

    <rect class="lower-panel" x="0" y="628" width="1200" height="233" fill="var(--night)"/>
    <rect class="mesh-area" x="0" y="630" width="1200" height="231" fill="url(#meshGlow)"
          role="img" aria-label="Dark abstract wave of connected network points"/>
    <line x1="0" y1="628.5" x2="1200" y2="628.5" stroke="var(--white)" stroke-width="1.2"/>
  </svg>

  <h1 class="headline">How much<br>are you loosing.....?</h1>

  <div class="brand">
    <div class="brand-mark">
      <span class="brand-name">quorvadetta</span>
      <span class="brand-dot"></span>
    </div>
    <p class="brand-tagline">BUILD SIGNAL, STAY CONNECTED</p>
  </div>
</main>
</body>
</html>
```